Business Card Design for Orthopaedic Surgeon

This is a double-sided glossy business card. I prefer baby blue, teal, and green as color schemes. I have my logo already (many colors that you can choose from). I have photos and examples of my old card (very bland but has the information in it). I also have one that my assistant tried to design, but the writing is too small and I don't love the formatting. But it is close!
I would like my logo to be on the business card but I'm uploading my logo in many different colors so you can choose which one looks best based on the color scheme. I also uploaded many sized headshots so you can choose the best resolution one.

Additional information:
Correct business address:
4382 NW 58th Lane, Suite 305
Tamarac, FL 33417

Everything else on both business cards are accurate.

I actually need 2 different business cards generated. One that includes my cell phone number-- Personal cell: 585-314-9062 in addition to Office phone: (954) 316-4870 and Office Fax: 954-316-4881. Again, one card would have my personal cell and one wouldn't

Overall I just think the baby blue card (uploaded) is missing something on the front--of course it is also missing my office phone/fax/personal cell. I do want my website on the front too. Email: info@wellsorthocare.example

You can use your discretion about what goes on the front vs. what goes on the back to eliminated clutter.

Oh and on the back, I would like to list "Conditions Treated" (not specialties include). The list is:
Carpal Tunnel
Trigger Finger
Ganglion Cysts
Hand Tumors
Han & Wrist Arthritis
Hand, Wrist & Elbow Tendonitis
Fractures of the Hand, Wrist, Elbow and Humerus
Nerve Injuries of the Hand, Wrist & Elbow
Microsurgery
Wrist Arthroscopy
Endoscopic Surgery

Target Market(s)

Primary care doctors, Lawyers, patients

Industry/Entity Type

Medical

Contact Information for Business Card

Please see above in project description

Colors

Designer to choose colors to be used in the design.

Requirements
Must have
• -Correct office info, Board Certified Orthopaedic Hand & Upper Extremity Surgeon
Nice to have
• Something that is classy and wow!

```html
<!DOCTYPE html>
<html lang="en">
<head>
<meta charset="utf-8">
<title>Danielle Wells, MD – Business Card</title>
<link href="https://fonts.googleapis.com/css2?family=Poppins:wght@600&family=Source+Sans+3:wght@400;600&display=swap" rel="stylesheet">
<style>
  :root {
    --brand-blue: #1199d6;
    --name-blue: #1a94d2;
    --ink: #222222;
    --paper: #ffffff;
    --stage: #1d1d1d;
    --rule: rgba(255,255,255,0.55);
    --portrait-dark: #3b2a23;
    --portrait-mid: #6b4a3a;
  }
  * { box-sizing: border-box; margin: 0; padding: 0; }
  html, body { width: 1093px; height: 1200px; overflow: hidden; }
  body {
    background: var(--stage);
    font-family: "Source Sans 3", "Myriad Pro", sans-serif;
    position: relative;
  }
  .card { position: absolute; left: 264px; overflow: hidden; }

  /* Front */
  .card-front { top: 226px; width: 578px; height: 357px; background: var(--paper); }
  .brand {
    position: absolute; left: 26px; top: 60px;
    display: flex; align-items: center; gap: 10px;
  }
  .brand-mark {
    width: 34px; height: 34px; border-radius: 50%;
    border: 3px solid var(--brand-blue);
  }
  .brand-name {
    font-family: "Poppins", sans-serif; font-weight: 600;
    font-size: 24px; letter-spacing: 1px; color: var(--brand-blue);
  }
  .doctor-name {
    position: absolute; left: 28px; top: 148px;
    font-family: "Poppins", sans-serif; font-weight: 600;
    font-size: 21px; color: var(--name-blue); letter-spacing: 0.2px;
  }
  .doctor-title {
    position: absolute; left: 28px; top: 181px;
    font-size: 16.5px; line-height: 21px; color: var(--ink);
  }
  .portrait {
    position: absolute; left: 375px; top: 18px; width: 203px; height: 218px;
    background: linear-gradient(180deg, var(--portrait-mid) 0%, var(--portrait-dark) 100%);
    border-radius: 90px 90px 0 0;
  }
  .contact-band {
    position: absolute; left: 0; top: 236px; width: 100%; height: 121px;
    background: var(--brand-blue); color: var(--paper);
  }
  .contact-row {
    position: absolute; left: 26px; display: flex; align-items: center; gap: 16px;
    font-size: 15px; white-space: nowrap;
  }
  .contact-row.row-one { top: 21px; }
  .contact-row.row-two { top: 42px; }
  .contact-item { display: flex; align-items: center; gap: 7px; }
  .contact-item svg { width: 15px; height: 15px; flex: none; }
  .address { position: absolute; left: 28px; top: 76px; font-size: 16px; }

  /* Back */
  .card-back { top: 620px; width: 582px; height: 357px; background: var(--brand-blue); color: var(--paper); }
  .section-title {
    position: absolute; left: 60px; top: 76px; width: 442px;
    display: flex; align-items: center; gap: 8px;
    font-family: "Poppins", sans-serif; font-weight: 600; font-size: 20px;
    white-space: nowrap;
  }
  .section-title::before, .section-title::after {
    content: ""; flex: 1; height: 1px; background: var(--rule);
  }
  .conditions {
    position: absolute; top: 156px; list-style: none;
    font-size: 17px; line-height: 15px;
  }
  .conditions.col-left { left: 84px; }
  .conditions.col-right { left: 297px; }
  .conditions li { position: relative; padding-left: 14px; margin-bottom: 6.7px; }
  .conditions li::before {
    content: ""; position: absolute; left: 0; top: 5px;
    width: 6px; height: 6px; border-radius: 50%; background: var(--paper);
  }
</style>
</head>
<body>

<section class="card card-front">
  <div class="brand">
    <span class="brand-mark"></span>
    <span class="brand-name">WELLS HAND</span>
  </div>
  <h1 class="doctor-name">DANIELLE WELLS, MD</h1>
  <p class="doctor-title">Board Certified Orthopaedic Hand &amp;<br>Upper Extremity Surgeon</p>
  <div class="portrait" role="img" aria-label="Headshot of the surgeon in a dark blazer"></div>

  <div class="contact-band">
    <div class="contact-row row-one">
      <span class="contact-item">
        <svg viewBox="0 0 16 16" fill="currentColor"><path d="M3.5 1l2.5 3-1.5 1.5c.8 2 2.5 3.7 4.5 4.5L10.5 8.5l3 2.5-1.5 3C7 14 2 9 2 2.5z"/></svg>
        585-314-9062
      </span>
      <span class="contact-item">
        <svg viewBox="0 0 16 16" fill="none" stroke="currentColor" stroke-width="1.6"><rect x="4" y="1" width="8" height="14" rx="1.5"/><line x1="7" y1="12.5" x2="9" y2="12.5"/></svg>
        (954) 316-4870
      </span>
    </div>
    <div class="contact-row row-two">
      <span class="contact-item">
        <svg viewBox="0 0 16 16" fill="currentColor"><rect x="4" y="1" width="8" height="4"/><rect x="1" y="5.5" width="14" height="6" rx="1"/><rect x="4" y="10" width="8" height="5" fill="var(--brand-blue)" stroke="currentColor" stroke-width="1.4"/></svg>
        954-316-4881
      </span>
      <span class="contact-item">
        <svg viewBox="0 0 16 16" fill="none" stroke="currentColor" stroke-width="1.5"><rect x="1.5" y="3.5" width="13" height="9"/><path d="M1.5 3.5l6.5 5.5 6.5-5.5"/></svg>
        info@wellsorthocare.example
      </span>
      <span class="contact-item">
        <svg viewBox="0 0 16 16" fill="none" stroke="currentColor" stroke-width="1.3"><circle cx="8" cy="8" r="6.5"/><ellipse cx="8" cy="8" rx="3" ry="6.5"/><line x1="1.5" y1="8" x2="14.5" y2="8"/><line x1="2.5" y1="4.8" x2="13.5" y2="4.8"/><line x1="2.5" y1="11.2" x2="13.5" y2="11.2"/></svg>
        www.wellsortho.example
      </span>
    </div>
    <p class="address">4382 NW 58th Lane, Suite 305, Tamarac, FL 33417</p>
  </div>
</section>

<section class="card card-back">
  <h2 class="section-title">CONDITIONS TREATED</h2>
  <ul class="conditions col-left">
    <li>Carpal Tunnel</li>
    <li>Trigger Finger</li>
    <li>Ganglion Cysts</li>
    <li>Hand Tumors</li>
    <li>Han &amp; Wrist Arthritis</li>
    <li>Hand, Wrist &amp; Elbow<br>Tendonitis</li>
  </ul>
  <ul class="conditions col-right">
    <li>Fractures of the Hand<br>Wrist, Elbow and Humerus</li>
    <li>Nerve Injuries of the Hand<br>Wrist &amp; Elbow</li>
    <li>Microsurgery</li>
    <li>Wrist Arthroscopy</li>
    <li>Endoscopic Surgery</li>
  </ul>
</section>

</body>
</html>
```